" A Veltrana TI é uma empresa Brasileira que atua em todo o território nacional e com projetos internacionais (França e Espanha). Nosso negócio principal é a Implantaçao, Administraçao e Suporte técnico em infraestrutura de TI (Servidores de e-mails, Servidores de Bancos de Dados, Servidores de Arquivos, Servidores WEB, estaçoes, ativos de rede, firewalls, virtualizaçao, nuvem, IaaS, SaaS e etc.) envolvendo soluçoes dos maiores fabricantes mundiais. Entregamos nossos serviços com Consultorias, Contratos de Suporte, Projetos e Serviços especializados com profissionais certificados. "

```html
<!DOCTYPE html>
<html lang="pt-BR">
<head>
<meta charset="UTF-8">
<title>Veltrana TI – Pasta Institucional</title>
<link href="https://fonts.googleapis.com/css2?family=Questrial&display=swap" rel="stylesheet">
<style>
  :root {
    --bg: #eef0f2;
    --paper: #f7f8f9;
    --paper-shade: #e9ebed;
    --grey: #8d8f92;
    --grey-light: #a9abae;
    --navy: #1f1f5c;
    --ink: #58595c;
    --white: #ffffff;
  }
  * { margin: 0; padding: 0; box-sizing: border-box; }
  html, body { width: 1200px; height: 1200px; overflow: hidden; }
  body {
    background: var(--bg);
    font-family: "Questrial", "Century Gothic", sans-serif;
    color: var(--ink);
    position: relative;
  }
  .spread {
    position: absolute;
    left: 210px;
    width: 780px;
    display: flex;
    box-shadow: 0 10px 30px rgba(0,0,0,0.12);
  }
  .spread--outside { top: 50px; height: 500px; }
  .spread--inside { top: 590px; height: 420px; }
  .panel { position: relative; width: 50%; height: 100%; overflow: hidden; }

  .back-cover { background: var(--grey); border-bottom: 10px solid var(--navy); }
  .back-cover .brand { position: absolute; left: 40px; bottom: 70px; }
  .back-cover .brand-name { font-size: 20px; color: var(--white); }
  .back-cover .brand-dot { background: var(--white); width: 14px; height: 14px; }
  .back-cover .contact {
    position: absolute; left: 40px; bottom: 22px;
    font-size: 9px; line-height: 1.4; color: var(--white); list-style: none;
  }

  .front-cover {
    background: linear-gradient(135deg, var(--white), var(--paper-shade));
    border-bottom: 10px solid var(--navy);
  }
  .front-cover .brand { position: absolute; left: 120px; top: 150px; }
  .front-cover .brand-name { font-size: 40px; }
  .front-cover .brand-dot { width: 26px; height: 26px; }

  .brand { display: flex; align-items: center; gap: 10px; }
  .brand-dot { display: inline-block; border-radius: 50%; background: var(--ink); }
  .brand-name { color: var(--ink); letter-spacing: 0.5px; line-height: 1; }

  .inside-left { background: linear-gradient(160deg, var(--paper), var(--paper-shade)); }
  .inside-right { background: linear-gradient(200deg, var(--white), var(--paper-shade)); }
  .pocket { position: absolute; left: 0; bottom: 0; width: 100%; height: 160px; }
  .pocket .brand { position: absolute; right: 26px; bottom: 82px; }
  .pocket .brand-name { font-size: 20px; color: var(--white); }
  .pocket .brand-dot { width: 14px; height: 14px; background: var(--white); }

  .signature {
    position: absolute; top: 1060px; left: 0; width: 100%;
    display: flex; justify-content: center;
  }
  .signature .brand-name { font-size: 44px; }
  .signature .brand-dot { width: 28px; height: 28px; }

  .footer-band {
    position: absolute; left: 0; bottom: 0; width: 100%; height: 14px;
    background: var(--navy);
  }
</style>
</head>
<body>
  <section class="spread spread--outside" aria-label="Capa da pasta">
    <div class="panel back-cover">
      <div class="brand"><span class="brand-dot"></span><span class="brand-name">Veltrana</span></div>
      <ul class="contact">
        <li>Av. Paulista Nova, 1500</li>
        <li>São Paulo – SP</li>
        <li>www.veltrana.com.br</li>
      </ul>
    </div>
    <div class="panel front-cover">
      <div class="brand"><span class="brand-dot"></span><span class="brand-name">Veltrana</span></div>
    </div>
  </section>

  <section class="spread spread--inside" aria-label="Interior da pasta">
    <div class="panel inside-left"></div>
    <div class="panel inside-right">
      <svg class="pocket" viewBox="0 0 390 160" preserveAspectRatio="none" aria-hidden="true">
        <polygon points="0,40 390,40 390,160 0,160" fill="#e4e6e8"/>
        <polygon points="0,40 120,40 95,160 0,160" fill="#1f1f5c"/>
        <polygon points="128,40 390,40 390,95 116,95" fill="#a9abae"/>
        <polygon points="120,40 128,40 104,160 95,160" fill="#ffffff"/>
      </svg>
      <div class="pocket">
        <div class="brand"><span class="brand-dot"></span><span class="brand-name">Veltrana</span></div>
      </div>
    </div>
  </section>

  <div class="signature">
    <div class="brand"><span class="brand-dot"></span><span class="brand-name">Veltrana</span></div>
  </div>
  <div class="footer-band"></div>
</body>
</html>
```